Leading the way in online fitness and education requires power house web design

If you need to contact me you can do so via
skype: Drembal

We need a website designed for new company based in Houston Texas called "DrembalFit". We offer web based training and nutrition programs for our members for example we use the same software as these companies: http://marlowquist.com/ http://www.liftrova.com/ i would like my visitors to be captivated by the level of design creativity of the site.

colors to use would be grey, orange and green.
for example i like the green of this site http://www.cartiva.com/
i will upload my logo files so you can get a feel for shades of grey and orange.

there is a 3d effect filter i would like applied to my logo for use in the web design i have uploaded what that effect looks like.

i will need your designs to be complete with all interior pages which will include Home, Fitness, Nutrition, Fit Lounge, Fit Score, Fit School, Contact Us, Sign up.

fit lounge on my site is the same as pacebin on liftrova and locker room on marlowquist just re branded.

fit school is a research corner for members to learn about health and fitness, we are members of major medical journals on health and fitness and will have all our articles be from the newest research findings.

competitor sites
these sites use same software:
http://marlowquist.com/
http://www.liftrova.com/

these sites are other software.
http://home.stridelogix.com/software-for-athletes.aspx
http://www.vaultrix.com/

here are some websites that i like:
http://www.quorvamedia.com/
http://www.nib-forge.com/
http://velbun.com/
http://www.pralvix.com/
http://www.tormelix.de/fandoloo/
http://brewickstudio.com/

i also like the greens in this site that i am uploading
Updates

I have been reviewing the designs and would like to update everyone at once I do not want a normal fitness website design style, no testimonials, blog post, bodyfat calculator

my website will be a membership based website. i want the website to sell the main points of my fitness app that my members will have access to look at the comments for my selling points, use those points in the site create designs and graphics to visualize those points.

look at these sites and gain inspiration

http://www.dumelo.com.pl/#/projekty/case-studies
http://www.corvane.com/en#/home#ld-qpxn-604217-0039
http://www.nib-forge.com/
http://velbun.com/
http://www.pralvix.com/

i have a few designers asking me what the selling points are, the website needs to be built around these points

main selling points.

overview

programs utilize the best multi-joint exercises combined with high intensity cardio, to give you a full-body workout, efficiently and effectively. This means you’re burning more calories and building more lean muscle per unit of time than traditional weight training and cardio programs.

When you sign up, you''ll receive a work out and diet plan to fit your goals and fitness level. As you progress through your plan, you can use the personal fitness and meal calendar to record your results. When you sign-up we''ll ask you a series of questions and your workouts will be tailored to your exact needs. That means never having to use a generic diet and exercise plan again.

If you''ve ever tried to lose weight and build muscle and didn''t succeed, we feel your pain. Until now, trying to navigate all the fitness fads and latest trends on your own has been difficult. The best option - hiring a certified personal trainer - may be out of your financial reach. That''s where we come in - we''re personal trainers on a mission to help you reach your fitness goals quickly and for less money than in person training. Best of all, we''re here to help you day or night.

Fitness

Personal Fitness Calendar

Tailored to the member’s schedule and flexible to accommodate any changes to a member’s regular fitness schedule. Track your progress and stay on track with your fitness goals.

Custom Fitness Plan

Based on a member’s current physical condition and goals.

• Step by step exercise instructions
• 3-D video demonstrations of over 600 exercises, including functional and body-weight only movements
• Equipment filter can customize plans to your gym’s equipment package
• Record workouts to track exercise history and progression

Nutrition

Nutritional Assessment

Daily recommended caloric intake (Protein, Carbohydrates and Fats), based on personal profile and daily fitness plan.

Custom Meal Plan

Personalized meal plan based on nutritional assessment.

• Choose number of meals per day
• Add dietary restrictions, food preferences or dislikes
• Database of thousands of ingredients allows for hundreds of thousands of meal combinations
• Include favorite foods by entering custom nutritional information

Weight tracking

Calculate goal weight and track weight-loss or weight-gain progress. You will reach your goals in no time.

Fit Lounge

What is the most important part of any workout or fitness program? Staying motivated. And what better form of motivation than positive encouragement from your peers?

Fit Lounge is fitness focused social network for health-minded individuals looking for a simple and convenient place to track their workout goals and monitor their progress. A unique system of motivation, support and accountability makes setting fitness goals and then keeping up with them easy

Track

Start by setting fitness goals that you want to track. They can be anything from running and jogging to how many hours of sleep you are getting and how many glasses of water you are drinking every day. Other members of the drembalfits community might be tracking the same workout goals as you, so you can always join their groups as well.

Share

Once you start tracking your workout goals, you can share your progress with your friends. Reach a new max on your bench press? Let everyone know. Eclipse the 10 mile mark on your daily run? Spread the word! The communication of encouragement back and forth is a great way to ensure that everyone stays on track with their workout goals.

Achieve

Of course, the point of any workout or fitness program is to achieve the goals you’ve set. And with help from drembalfits workout tracking tools and encouragement from the community, you will achieve your workout goals in no time. When you see a friend has achieved his or her fitness goals, you can send them a virtual “fist bump” as a sign of congratulations. The number of “fist bumps” each user accumulates will be displayed on their profile, providing additional motivation and a healthy dose of competition.

Reason: i dont feel the designs i have received are of the quality i am looking for

check this website out, i know its flash, but i also know you can get creative without flash and have nice effects throughout the site.

http://www.lanterfold-hub.com/

I dont want plain jane designs, insert the content i provided into the site and have it explored in a unique way. take as much time on the design as you need as i will keep extending deadline until i find one that is perfect.

as said before don't make the site anything like the competition sites, its only purpose is to sell the memberships using content provided so i need an innovative way to for them to explore that content,

as your designing this site add me on skype so i can detail and help brainstorm ideas my skype id is drembal
you can stray from the color scheme a little or throw it away if you want i just want to see how creative you can get.

Industry/Entity Type

School

Requirements
Nice to have
• if you notice at the bottom of http://marlowquist.com/ she has the orange bar with the three short content parts, i like the idea of having a space like that for similar content.

on http://www.vaultrix.com/ if you look to the left side of the scrolling icons i like the idea of having icons or animated pictures to point of key benefits.

```html
<!DOCTYPE html>
<html lang="en">
<head>
<meta charset="utf-8">
<title>DrembalFit – Personal Training</title>
<link href="https://fonts.googleapis.com/css2?family=Arimo:wght@400;700&family=PT+Sans:wght@400;700&display=swap" rel="stylesheet">
<style>
:root{
  --bg:#eeeeee;
  --card:#ffffff;
  --green:#6ea51b;
  --green-light:#94c83a;
  --green-dark:#4f7e10;
  --orange:#e8651c;
  --orange-light:#f08a3c;
  --orange-dark:#c94f10;
  --grey-dark:#3b3b3b;
  --grey:#666666;
  --grey-mid:#9a9a9a;
  --line:#d9d9d9;
  --text:#333333;
  --red:#c8202a;
}
*{margin:0;padding:0;box-sizing:border-box}
html,body{width:753px;height:1200px;overflow:hidden;background:var(--bg);font-family:"Arimo",Arial,sans-serif;color:var(--text)}
.page{position:relative;width:753px;height:1200px}
.abs{position:absolute}
.card{left:24px;top:7px;width:705px;height:1153px;background:var(--card);box-shadow:0 0 10px rgba(0,0,0,.18)}
.brand{left:40px;top:42px;display:flex;align-items:center;gap:10px}
.brand-dot{width:26px;height:26px;border-radius:50%;background:var(--orange)}
.brand-name{font-family:"PT Sans",sans-serif;font-weight:700;font-size:38px;color:var(--grey-dark);letter-spacing:-.5px}
.login{left:540px;top:7px;width:167px;height:22px;background:linear-gradient(#f4f4f4,#dcdcdc);border-radius:0 0 12px 12px;font-size:11px;font-weight:700;color:var(--grey);display:flex;align-items:center;justify-content:center;gap:6px}
.login-dot{width:11px;height:11px;border-radius:50%;background:var(--red)}
.greeting{right:64px;top:50px;text-align:right;font-size:9px;line-height:17px}
.greeting b{color:var(--grey-dark)}
.basket{color:var(--green)}
.nav{left:35px;top:103px;width:677px;height:28px;display:flex;background:linear-gradient(var(--green-light),var(--green));border-radius:4px 4px 0 0}
.nav a{display:flex;align-items:center;justify-content:center;color:#fff;font-weight:700;font-size:11.5px;text-decoration:none;border-right:1px solid rgba(255,255,255,.35)}
.nav a.active{background:linear-gradient(var(--orange-light),var(--orange));color:var(--grey-dark);border-radius:4px 0 0 0}
.nav a:last-child{border-right:0}
.hero{left:35px;top:131px;width:677px;height:249px;background:linear-gradient(90deg,#8a8a8a,#555 45%,#3a3a3a);overflow:hidden}
.hero-photo{left:0;top:0;width:310px;height:249px;background:linear-gradient(90deg,#b9b9b9,#7a7a7a 70%,rgba(90,90,90,0))}
.hero-apple{left:365px;top:122px;width:82px;height:74px;border-radius:50%;background:radial-gradient(circle at 40% 35%,#c7e86a,#7eb228 70%);opacity:.9}
.hero-title{left:218px;top:24px;width:315px;white-space:nowrap;font-family:"PT Sans",sans-serif;font-weight:400;font-size:17.5px;letter-spacing:-.2px;color:#a9d64a}
.hero-copy{left:221px;top:53px;width:305px;font-size:12px;font-weight:700;color:#fff;line-height:18px}
.trial{left:315px;top:182px;width:167px;height:51px;background:linear-gradient(var(--orange-light),var(--orange-dark));border:2px solid #7a3a10;border-radius:3px;text-align:center;font-family:"PT Sans",sans-serif;font-weight:700;font-size:15px;line-height:20px;color:#fff;padding-top:4px}
.trial span{color:#c9f05a}
.thumbs{left:538px;top:0;width:139px;height:249px;background:#2e2e2e;padding:3px 3px}
.thumb{display:flex;align-items:center;gap:6px;height:44px;margin-bottom:4px;padding:0 4px;font-size:9.5px;color:#fff;line-height:12px;background:#444}
.thumb.on{background:var(--orange)}
.thumb i{display:block;width:48px;height:38px;background:linear-gradient(#c9c9c9,#8f8f8f);flex:none}
.band{left:35px;top:380px;width:677px;height:40px;background:linear-gradient(var(--orange-light),var(--orange-dark));border-radius:0 0 6px 6px;display:flex;align-items:center;gap:10px;padding-left:8px;font-family:"PT Sans",sans-serif;font-size:17.5px;color:#fff}
.band .sep{color:rgba(255,255,255,.7)}
h2.title{font-family:"PT Sans",sans-serif;font-size:17px;color:var(--grey-dark)}
h2.title span{color:var(--green)}
.welcome{left:35px;top:445px;width:495px}
.welcome .rule{height:1px;background:var(--line);margin:4px 0 6px}
.welcome p{font-size:8.6px;line-height:13px;color:var(--text)}
.welcome a{color:var(--text)}
.more{display:inline-flex;align-items:center;gap:4px;font-size:9px;font-weight:700;color:var(--grey-dark)}
.more i{width:10px;height:10px;border-radius:50%;background:var(--orange);display:inline-block;position:relative}
.more i::after{content:"";position:absolute;left:3px;top:2.5px;border-left:4px solid #fff;border-top:2.5px solid transparent;border-bottom:2.5px solid transparent}
.more-btn{display:inline-flex;align-items:center;gap:4px;padding:3px 5px 3px 7px;border:1px solid var(--line);border-radius:10px;background:linear-gradient(#fff,#ececec);font-size:9px;font-weight:700;color:var(--grey-dark)}
.box{border:1px solid var(--line);border-radius:5px;background:#fff}
.box-head{height:25px;background:linear-gradient(var(--green-light),var(--green));border-radius:5px 5px 0 0;color:#fff;font-family:"PT Sans",sans-serif;font-weight:700;font-size:15px;padding:3px 10px}
.box-head.tab{width:160px;border-radius:5px 5px 0 0}
.news{left:537px;top:453px;width:175px;height:254px}
.news-item{display:flex;gap:6px;padding:6px 5px 0;height:63px;border-bottom:1px solid #eee}
.news-item i{width:76px;height:50px;flex:none;border:1px solid var(--line);border-radius:6px;background:linear-gradient(#e8c2d8,#a67090)}
.news-item i.food{background:linear-gradient(#cde08d,#d86a4a)}
.news-item p{font-size:8.5px;font-weight:700;line-height:11px}
.news-item em{display:block;font-style:normal;font-weight:400;color:var(--green);text-align:center;margin-top:3px}
.news .more{position:absolute;right:10px;bottom:8px}
.workouts{left:39px;top:583px;width:491px;height:197px}
.wcol{position:absolute;top:30px;width:150px}
.wcol h3{font-weight:400;font-size:10.5px;color:var(--grey-dark);margin-bottom:4px}
.wcol .ph{height:72px;border-bottom:3px solid var(--green);background:linear-gradient(#d8d8d8,#8d8d8d)}
.wcol .ph.warm{background:linear-gradient(#c77a4a,#5a2e1a)}
.wcol p{font-size:8.6px;line-height:11.5px;margin:7px 0 9px}
.feature{top:792px;width:241px;height:184px}
.feature .row{display:flex;align-items:center;gap:10px;padding:14px 10px 0}
.feature .ph{width:92px;height:62px;flex:none;border-radius:50%;background:radial-gradient(circle at 40% 40%,#b8e04a,#6a9a1a 70%,#fff 72%)}
.feature .ph.mat{border-radius:6px;background:linear-gradient(#eef5f6,#9cc4c8)}
.feature h4{font-family:"PT Sans",sans-serif;font-weight:400;font-size:12.5px;line-height:15px;color:var(--green)}
.feature p{font-size:8.6px;line-height:11.5px;padding:10px 8px 6px}
.feature .more-btn{margin-left:8px}
.newsletter{left:537px;top:716px;width:175px;height:81px;background:linear-gradient(var(--green-light),var(--green-dark));border-radius:5px;padding:5px}
.newsletter .env{position:absolute;left:7px;top:8px;width:48px;height:38px;background:linear-gradient(#f6d77a,#e39a2a);transform:rotate(-12deg);border-radius:2px}
.newsletter h3{position:absolute;left:62px;top:5px;font-family:"PT Sans",sans-serif;font-size:14px;color:#fff;letter-spacing:.5px}
.newsletter p{position:absolute;left:62px;top:24px;width:108px;font-size:8px;line-height:10px;color:#fff}
.newsletter .field{position:absolute;left:5px;top:60px;width:118px;height:16px;background:#fff;font-size:7.5px;color:var(--grey-mid);padding:3px 4px}
.newsletter .btn{position:absolute;left:127px;top:60px;width:43px;height:16px;background:linear-gradient(#fff,#ddd);border-radius:2px;font-size:8.5px;font-weight:700;text-align:center;line-height:16px}
.videos-title{left:539px;top:802px;font-family:"PT Sans",sans-serif;font-size:15px;color:var(--orange)}
.video{left:537px;top:829px;width:175px;height:144px;border:1px solid var(--line)}
.video .ph{height:122px;background:linear-gradient(#fafafa,#dde4e6)}
.video .bar{height:20px;background:linear-gradient(#fdfdfd,#d8d8d8);display:flex;align-items:center;gap:6px;padding:0 5px}
.video .bar .play{border-left:7px solid #444;border-top:4px solid transparent;border-bottom:4px solid transparent}
.video .track{height:4px;border-radius:2px;background:#999;position:relative}
.video .knob{position:absolute;top:-3px;width:9px;height:9px;border-radius:50%;background:#555}
.promo{left:24px;top:989px;width:705px;height:160px;background:linear-gradient(var(--orange),var(--orange-dark));display:flex}
.promo-col{flex:1;padding:4px 12px 0 12px;border-right:1px solid rgba(255,255,255,.25);position:relative}
.promo-col:last-child{border-right:0}
.promo-col h3{display:inline-block;background:linear-gradient(var(--green-light),var(--green));color:#fff;font-family:"PT Sans",sans-serif;font-size:14px;padding:4px 8px;border-radius:3px;margin-left:-2px}
.promo-col p{font-size:8.4px;line-height:11.5px;color:#fff;margin-top:8px}
.promo-col .rm{position:absolute;right:14px;bottom:9px;font-size:8.5px;font-weight:700;color:#fff;display:flex;align-items:center;gap:4px}
.promo-col .rm i{width:8px;height:8px;border-radius:50%;background:var(--green-light)}
.foot-nav{left:40px;top:1177px;display:flex;gap:13px;font-size:9px;color:var(--grey)}
.foot-nav .active{color:var(--orange)}
.copy{right:46px;top:1177px;font-size:8.5px;color:var(--grey)}
.copy b{color:var(--grey-dark)}
</style>
</head>
<body>
<div class="page">
  <div class="abs card"></div>

  <div class="abs brand"><span class="brand-dot"></span><span class="brand-name">DrembalFit</span></div>
  <div class="abs login"><span class="login-dot"></span>Log in or Sign Up</div>
  <div class="abs greeting"><b>Hello,Welcome To DrembalFit</b><br><span class="basket">&#9632; Shopping basket <b style="color:var(--orange)">0 items</b></span></div>

  <nav class="abs nav">
    <a class="active" style="width:72px">Home</a>
    <a style="width:90px">Fitness</a>
    <a style="width:103px">Nutrition</a>
    <a style="width:107px">Fit Lounge</a>
    <a style="width:100px">Fit Score</a>
    <a style="width:106px">Fit School</a>
    <a style="width:99px">Contact Us</a>
  </nav>

  <section class="abs hero">
    <div class="abs hero-photo" role="img" aria-label="Trainer coaching a man lifting dumbbells in a gym"></div>
    <div class="abs hero-apple" role="img" aria-label="Green apples"></div>
    <h1 class="abs hero-title">When You're Serious About Getting Fit.</h1>
    <p class="abs hero-copy">Duis aute irure dolor in reprehenderit in voluptate velit esse cillum dolore eu fugiat nulla pariatur. Excepteur sint occaecat cupidatat non proident,</p>
    <div class="abs trial">See results during your<br><span>Free 15-day trial</span></div>
    <div class="abs thumbs">
      <div class="thumb on"><i role="img" aria-label="Gym training"></i>Lorem ipsum dolor sit amet</div>
      <div class="thumb"><i role="img" aria-label="Stretching"></i>Lorem ipsum dolor sit amet</div>
      <div class="thumb"><i role="img" aria-label="Workout class"></i>Lorem ipsum dolor sit amet</div>
      <div class="thumb"><i role="img" aria-label="Healthy food"></i>Lorem ipsum dolor sit amet</div>
      <div class="thumb"><i role="img" aria-label="Dumbbell exercise"></i>Lorem ipsum dolor sit amet</div>
    </div>
  </section>

  <div class="abs band">Ready to Get Fit ? <span class="sep">&#x232A;</span> Track all your training, nutrition and metrics <span class="sep">&#x232A;</span> Reach Goals</div>

  <section class="abs welcome">
    <h2 class="title">Welcome to <span>DrembalFit</span></h2>
    <div class="rule"></div>
    <p><b>Lorem ipsum dolor sit amet,</b> consectetuer adipiscing elit, sed diam nonummy nibh euismod tincidunt ut laoreet dolore magna aliquam erat volutpat. Ut wisi enim ad minim veniam, quis nostrud exerci tation ullamcorper suscipit lobortis nisl ut aliquip ex ea commodo consequat. Duis autem vel eum iriure dolor in hendrerit in vulputate velit esse molestie consequat, vel illum dolore eu feugiat nulla facilisis at vero eros et accumsan et iusto odio dignissim qui blandit praesent luptatum zzril delenit augue duis dolore te feugait nulla facilisi <a>Lorem ipsum dolor sit amet</a>, consectetuer adipiscing elit, sed diam nonummy nibh euismod tincidunt ut laoreet dolore magna aliquam erat volutpat.</p>
    <div style="text-align:right;margin-top:3px"><span class="more"><i></i>Read more</span></div>
  </section>

  <aside class="abs box news">
    <div class="box-head">Latest News</div>
    <div class="news-item"><i role="img" aria-label="Woman exercising"></i><p>Lorem ipsum dolor sit amet consect adipisicing elit, sed<em>Feb 22,2012</em></p></div>
    <div class="news-item"><i class="food" role="img" aria-label="Fresh vegetables"></i><p>Lorem ipsum dolor sit amet consect adipisicing elit, sed<em>Feb 12,2012</em></p></div>
    <div class="news-item"><i role="img" aria-label="Woman with dumbbells"></i><p>Lorem ipsum dolor sit amet consect adipisicing elit, sed<em>Jan 28,2012</em></p></div>
    <span class="more"><i></i>More news</span>
  </aside>

  <section class="abs box workouts">
    <div class="box-head">Latest Workouts</div>
    <div class="wcol" style="left:7px"><h3>Ddumbbell Workouts</h3><div class="ph" role="img" aria-label="Man doing dumbbell workout"></div><p>Excepteur sint occaecat cupidatat non proident, sunt in culpa deserunt mollit anim id est laborum.</p><span class="more-btn">Read more <span class="more"><i></i></span></span></div>
    <div class="wcol" style="left:170px"><h3>Bodybuilding Workout</h3><div class="ph warm" role="img" aria-label="Woman lifting a dumbbell"></div><p>Excepteur sint occaecat cupidatat non proident, sunt in culpa deserunt mollit anim id est laborum.</p><span class="more-btn">Read more <span class="more"><i></i></span></span></div>
    <div class="wcol" style="left:334px"><h3>Fat Burning Workout</h3><div class="ph" role="img" aria-label="People on exercise bikes"></div><p>Excepteur sint occaecat cupidatat non proident, sunt in culpa deserunt mollit anim id est laborum.</p><span class="more-btn">Read more <span class="more"><i></i></span></span></div>
  </section>

  <section class="abs box feature" style="left:39px">
    <div class="box-head tab">Nutrition</div>
    <div class="row"><div class="ph" role="img" aria-label="Green apple with measuring tape"></div><h4>Lorem ipsum dolor sit amet consectetur adipiscing</h4></div>
    <p>Duis aute irure dolor in reprehenderit in voluptate velit esse cillum dolore eu fugiat nulla pariatur. Excepteur occaecat cupidatat non proident, sunt in culpa qui officia deserunt mollit anim id est laborum.</p>
    <span class="more-btn">Read more <span class="more"><i></i></span></span>
  </section>

  <section class="abs box feature" style="left:289px">
    <div class="box-head tab">Fitness</div>
    <div class="row"><div class="ph mat" role="img" aria-label="Woman stretching on a mat"></div><h4>Duis aute irure dolor in reprehenderit in voluptate velit</h4></div>
    <p>Lorem ipsum dolor sit amet, consectetur adipiscing elit. Morbi id tristique sem. Nunc nec ipsum sed nisi dictum mollis. Praesent malesuada mauris a odio adipiscing mollis. In varius tincidunt elit vitae eleifend.</p>
    <span class="more-btn">Read more <span class="more"><i></i></span></span>
  </section>

  <div class="abs newsletter">
    <div class="env" role="img" aria-label="Envelope"></div>
    <h3>NEWSLETTER</h3>
    <p>New Excercises,Fitness and your diet plans to your email.</p>
    <div class="field">Type your email here...</div>
    <div class="btn">Submit</div>
  </div>

  <h2 class="abs videos-title">Fitness Videos</h2>
  <div class="abs video">
    <div class="ph" role="img" aria-label="Woman stretching, video still"></div>
    <div class="bar"><span class="play"></span><div class="track" style="width:95px"><span class="knob" style="left:58px"></span></div><span style="font-size:8px">&#9632;</span><div class="track" style="width:28px"><span class="knob" style="left:14px"></span></div></div>
  </div>

  <section class="abs promo">
    <div class="promo-col"><h3>Create your own exercise</h3><p>Lorem ipsum dolor sit amet, consectetuer adipiscing elit, sed diam nonummy nibh euismod tincidunt ut laoreet dolore magna aliquam erat volutpat. Ut wisi enim ad minim veniam, quis nostrud exerci tation ullamcorper suscipit lobortis nisl ut aliquip ex ea commodo consequat. Duis autem vel eum iriure dolor in hendrerit in vulputate velit esse molestie consequat</p><span class="rm"><i></i>Read more</span></div>
    <div class="promo-col"><h3>Personal Fitness Calendar</h3><p>Lorem ipsum dolor sit amet, consectetuer adipiscing elit, sed diam nonummy nibh euismod tincidunt ut laoreet dolore magna aliquam erat volutpat. Ut wisi enim ad minim veniam, quis nostrud exerci tation ullamcorper suscipit lobortis nisl ut aliquip ex ea commodo consequat. Duis autem vel eum iriure dolor</p><span class="rm"><i></i>Read more</span></div>
    <div class="promo-col"><h3>A Workout &amp; Diet Plan</h3><p>Lorem ipsum dolor sit amet, consectetuer adipiscing elit, sed diam nonummy nibh euismod tincidunt ut laoreet dolore magna aliquam erat volutpat. Ut wisi enim ad minim veniam, quis nostrud exerci tation ullamcorper suscipit lobortis nisl ut aliquip ex ea commodo consequat.</p><span class="rm"><i></i>Read more</span></div>
  </section>

  <footer>
    <nav class="abs foot-nav"><span class="active">Home</span><span>Fitness</span><span>Nutrition</span><span>Fit Lounge</span><span>Fit Score</span><span>Fit School</span><span>Contact Us</span></nav>
    <div class="abs copy">Copyright © 2012 <b>DrembalFit</b> All rights reserved</div>
  </footer>
</div>
</body>
</html>
```